Business Card for New Greek Restaurant

Looking for a Business card for a new Greek Restaurant that's focus is on Take out and Delivery & catering.

Also to outline the contact information for the restaurant.
Does not require a name or title of a specific person (Just general business card)
Phone (519) 731-FOOD (3663)
Email : info@bluefigkitchen.ca
Website : www.bluefigkitchen.ca

Facebook/Instagram/Twitter Icons to Follow us as well.

TAKEOUT * DELIVERY* CATERING

Target Market(s)

Woman Age 25-44

Industry/Entity Type

Greek Restaurant

Contact Information for Business Card

Card is to have the general contact information for the business as well as outline our Take Out and Catering Services. Existing Logo attached and to be incorporated into the design.

Font styles to use
Sans Serif

Colors

Designer to choose colors to be used in the design.

Requirements
Must have
• Restaurant Contact Information :
• Phone (519) 731-FOOD (3663)
• Email : info@bluefigkitchen.ca
• Website : www.bluefigkitchen.ca
• Highlight Takeout, Catering, Delivery
• Business Address :
• Maplerow Plaza
• 47 Carden Ave., Unit 6
• Breslau ON
• N0K 2P5
Nice to have
• Modern Feel to promote TakeOut and Catering Services.
Should not have
• No Specific Title or Contact Person (Generic Business Card for Restaurant)

```html
<!DOCTYPE html>
<html lang="en">
<head>
<meta charset="utf-8">
<title>Blue Fig Kitchen – Business Card</title>
<link rel="stylesheet" href="https://fonts.googleapis.com/css2?family=Montserrat:wght@300;400;600&display=swap">
<style>
  :root {
    --sky: #1fbfea;
    --sky-deep: #15b4e2;
    --white: #ffffff;
    --paper: #fbfbfb;
    --stage: #2a2a2a;
    --ink-soft: rgba(255,255,255,0.92);
  }
  * { box-sizing: border-box; margin: 0; padding: 0; }
  html, body { width: 1200px; height: 900px; overflow: hidden; }
  body {
    background: var(--stage);
    font-family: "Montserrat", sans-serif;
    position: relative;
  }
  .card {
    position: absolute;
    width: 620px;
    height: 354px;
    border-radius: 22px;
    box-shadow: 0 14px 34px rgba(0,0,0,0.45);
    overflow: hidden;
  }
  /* front */
  .card-front {
    left: 140px; top: 80px;
    background: linear-gradient(135deg, var(--sky) 0%, var(--sky-deep) 100%);
    color: var(--white);
  }
  .brand {
    display: flex;
    align-items: center;
    gap: 12px;
  }
  .brand-dot {
    width: 16px; height: 16px; border-radius: 50%;
  }
  .brand-name {
    font-weight: 600;
    text-transform: uppercase;
    letter-spacing: 2px;
    line-height: 1;
  }
  .card-front .brand {
    position: absolute; right: 48px; top: 62px;
  }
  .card-front .brand-dot { background: var(--white); }
  .card-front .brand-name { font-size: 34px; color: var(--white); }
  .card-front .tagline {
    position: absolute; right: 50px; top: 112px;
    font-size: 13px; font-weight: 300; letter-spacing: 7px;
    text-transform: uppercase;
  }
  .services {
    position: absolute; right: 48px; bottom: 64px;
    font-size: 21px; font-weight: 300; letter-spacing: 0.5px;
    color: var(--ink-soft);
    text-transform: uppercase;
    display: flex; gap: 16px;
  }
  .services .sep { opacity: 0.85; }

  /* back */
  .card-back {
    left: 440px; top: 466px;
    background: linear-gradient(135deg, var(--white) 0%, var(--paper) 70%, #eeeeee 100%);
    color: var(--sky);
  }
  .card-back .brand {
    position: absolute; left: 42px; top: 140px;
    flex-direction: column; align-items: flex-start; gap: 10px;
  }
  .card-back .brand-row { display: flex; align-items: center; gap: 10px; }
  .card-back .brand-dot { background: var(--sky); width: 12px; height: 12px; }
  .card-back .brand-name { font-size: 24px; color: var(--sky); }
  .card-back .tagline {
    font-size: 10px; font-weight: 300; letter-spacing: 6px; text-transform: uppercase;
    padding-left: 22px;
  }
  .contact {
    position: absolute; left: 330px; top: 60px;
    font-size: 14px; font-weight: 400; line-height: 1.55;
  }
  .rule {
    width: 70px; height: 3px; background: var(--sky);
  }
  .rule-top { margin-bottom: 14px; }
  .rule-bottom { margin-top: 16px; }
  .contact-row { display: flex; align-items: flex-start; gap: 8px; }
  .contact-row svg { width: 13px; height: 13px; margin-top: 4px; flex: none; fill: var(--sky); }
  .address-lines { display: flex; flex-direction: column; }
  .website {
    position: absolute; left: 330px; bottom: 44px;
    font-size: 20px; font-weight: 400;
  }
</style>
</head>
<body>

  <section class="card card-front" aria-label="Card front">
    <div class="brand">
      <span class="brand-dot"></span>
      <span class="brand-name">Blue Fig Kitchen</span>
    </div>
    <p class="tagline">Fresh Grill</p>
    <p class="services">
      <span>Takeout</span><span class="sep">|</span>
      <span>Catering</span><span class="sep">|</span>
      <span>Delivery</span>
    </p>
  </section>

  <section class="card card-back" aria-label="Card back">
    <div class="brand">
      <div class="brand-row">
        <span class="brand-dot"></span>
        <span class="brand-name">Blue Fig Kitchen</span>
      </div>
      <p class="tagline">Fresh Grill</p>
    </div>

    <div class="contact">
      <div class="rule rule-top"></div>
      <div class="contact-row">
        <svg viewBox="0 0 24 24" aria-hidden="true"><path d="M6.6 10.8a15.1 15.1 0 0 0 6.6 6.6l2.2-2.2c.3-.3.7-.4 1-.2 1.1.4 2.3.6 3.6.6.6 0 1 .4 1 1V20c0 .6-.4 1-1 1A17 17 0 0 1 3 4c0-.6.4-1 1-1h3.5c.6 0 1 .4 1 1 0 1.3.2 2.5.6 3.6.1.3 0 .7-.2 1z"/></svg>
        <span>(519) 731-FOOD (3663)</span>
      </div>
      <div class="contact-row">
        <svg viewBox="0 0 24 24" aria-hidden="true"><path d="M2 5h20v14H2zm2 2v.4l8 5 8-5V7zm0 2.8V17h16V9.8l-8 5z"/></svg>
        <span>info@bluefigkitchen.ca</span>
      </div>
      <div class="contact-row">
        <svg viewBox="0 0 24 24" aria-hidden="true"><path d="M12 2a7 7 0 0 0-7 7c0 5.2 7 13 7 13s7-7.8 7-13a7 7 0 0 0-7-7zm0 9.5A2.5 2.5 0 1 1 12 6.5a2.5 2.5 0 0 1 0 5z"/></svg>
        <span class="address-lines">
          <span>Maplerow Plaza</span>
          <span>47 Carden Ave., Unit 6</span>
          <span>Breslau ON N0K 2P5</span>
        </span>
      </div>
      <div class="rule rule-bottom"></div>
    </div>

    <p class="website">www.bluefigkitchen.ca</p>
  </section>

</body>
</html>
```